New Dental Office Needs an Attractive and user friendly Website Designed

I need a website for a new dental office. The Name is Maplecrest Dentistry. I would like a Modern design with a user friendly interface and usability.
I would like a landing page, a page that lists the services we offer: Cosmetic Dentistry, Implants, Dental Hygiene, Emergency Services, Restorations, Dentures
Target Market(s)
Mid to upper class
Industry/Entity Type
Dentistry
Coding
Coded - Design and coding required
Number of Pages Required
1 page
Requirements
Must have
- Landing page that has a scheduling option, Procedures, operating hours, and contact us info
Nice to have
- Appealing design, Soft comforting colors. Easy to navigate page, Modern and professional.

```html
<!DOCTYPE html>
<html lang="en">
<head>
<meta charset="utf-8">
<title>Maplecrest Dentistry</title>
<link href="https://fonts.googleapis.com/css2?family=Lato:wght@400;700&family=Playfair+Display:wght@500;600;700&display=swap" rel="stylesheet">
<style>
:root{
  --teal:#5cc0b5;
  --teal-soft:#e5f3f1;
  --navy:#2d3e50;
  --ink:#1f2a36;
  --muted:#5d6873;
  --gold:#d6a93a;
  --bg:#f7f9fa;
  --white:#ffffff;
  --footer:#252322;
}
*{box-sizing:border-box;margin:0;padding:0}
html,body{width:1200px;height:3347px;overflow:hidden}
body{position:relative;background:var(--bg);font-family:'Lato',sans-serif;color:var(--ink)}
.abs{position:absolute}
a{text-decoration:none}
.logo{font-family:'Playfair Display',serif;font-weight:500;color:var(--white);font-size:20px;letter-spacing:.2px}

/* hero */
.hero{position:absolute;left:0;top:0;width:1200px;height:491px}
.hero-photo{position:absolute;inset:0;background:linear-gradient(100deg,#3d5766 0%,#5b7684 35%,#9fb2bb 65%,#c8d3d8 100%)}
.hero-shade{position:absolute;inset:0;background:linear-gradient(90deg,rgba(30,45,58,.65) 0%,rgba(30,45,58,.35) 45%,rgba(30,45,58,0) 70%)}
.nav{position:absolute;left:140px;top:29px;width:918px;height:50px;background:var(--footer);border-radius:8px;display:flex;align-items:center;justify-content:space-between;padding:0 21px}
.nav-links{display:flex;gap:29px;font-family:'Playfair Display',serif;font-size:13px;color:#e8e8e8}
.hero h1{position:absolute;left:140px;top:168px;font-family:'Playfair Display',serif;font-weight:700;font-size:46px;line-height:54px;color:var(--white)}
.hero h1 .accent{color:var(--teal);border-bottom:2px solid var(--gold)}
.hero p{position:absolute;left:140px;top:276px;font-size:13px;color:#f1f4f5}
.btn{display:inline-flex;align-items:center;justify-content:center;border-radius:4px;font-size:13px}
.btn-teal{background:var(--teal);color:var(--white)}
.btn-white{background:var(--white);color:var(--ink)}

.booking{position:absolute;left:140px;top:429px;width:918px;height:81px;background:var(--bg);border-radius:8px;box-shadow:0 6px 18px rgba(0,0,0,.08)}
.field{position:absolute;top:22px}
.field .lbl{font-family:'Playfair Display',serif;font-size:13px;color:var(--ink);margin-bottom:8px}
.field .val{font-size:12px;color:var(--ink);display:flex;align-items:center;gap:6px}
.divider{position:absolute;top:24px;width:1px;height:34px;background:#cdd3d8}

/* section headings */
.section-title{position:absolute;left:0;width:1200px;text-align:center;font-family:'Playfair Display',serif;font-weight:600;font-size:29px}
.section-title u{text-decoration:none;border-bottom:3px solid var(--gold)}
.section-sub{position:absolute;left:0;width:1200px;text-align:center;font-size:12.5px;line-height:16px}

/* services */
.svc{position:absolute;width:292px;height:188px;background:var(--teal-soft);border-radius:16px;padding:22px}
.svc .ico{width:42px;height:42px;border-radius:6px;background:var(--teal);display:flex;align-items:center;justify-content:center}
.svc h3{font-family:'Playfair Display',serif;font-weight:500;font-size:21px;margin-top:40px;color:var(--ink)}
.svc p{font-size:12.5px;line-height:16px;color:#333d47;margin-top:4px}

/* why */
.why{position:absolute;left:0;top:1145px;width:1200px;height:695px;background:var(--navy)}
.why-item{position:absolute;left:140px;width:424px;height:98px;background:var(--bg);border-radius:6px}
.why-item .ico{position:absolute;left:15px;top:15px;width:70px;height:68px;background:var(--teal-soft);border-radius:5px;display:flex;align-items:center;justify-content:center}
.why-item h3{position:absolute;left:100px;top:15px;font-family:'Playfair Display',serif;font-weight:500;font-size:21px}
.why-item p{position:absolute;left:100px;top:48px;width:305px;font-size:12.5px;line-height:16px;color:var(--muted)}
.why-photo{position:absolute;left:600px;top:1322px;width:468px;height:447px;border-top:10px solid var(--teal);border-right:10px solid var(--teal);border-radius:90px 0 110px 0;overflow:hidden}
.why-photo .fill{position:absolute;inset:0;background:linear-gradient(160deg,#cfd8dc 0%,#e9e4dc 45%,#b7c4cb 100%);border-radius:80px 0 100px 0}

/* visit */
.map{position:absolute;left:140px;top:2026px;width:642px;height:461px;background:linear-gradient(135deg,#9ec9ec 0%,#e6e8e3 40%,#f1eedf 70%,#b9d9f2 100%)}
.info{position:absolute;left:757px;top:2095px;width:301px;height:324px;background:var(--navy);border-radius:10px;padding:28px 28px;color:var(--white)}
.info h4{font-family:'Playfair Display',serif;font-weight:500;font-size:20px;display:flex;align-items:center;gap:6px}
.info p{font-size:12px;line-height:16px;margin-top:6px}

/* testimonials */
.reviews{position:absolute;left:0;top:2558px;width:1200px;height:511px;background:var(--navy)}
.review{position:absolute;top:2731px;width:448px;height:191px;background:var(--white);border-radius:10px;padding:22px 21px}
.review .stars{display:flex;gap:4px}
.review .date{position:absolute;right:22px;top:26px;font-size:12.5px}
.review .quote{margin-top:14px;font-size:12.5px;line-height:16px;color:#333d47}
.review .who{position:absolute;left:21px;top:114px;display:flex;align-items:center;gap:14px}
.avatar{width:55px;height:55px;border-radius:50%}
.review .name{font-family:'Playfair Display',serif;font-weight:500;font-size:21px}
.review .role{font-size:12px;color:var(--muted)}
.arrow{position:absolute;top:2816px;width:28px;height:28px;border-radius:4px;display:flex;align-items:center;justify-content:center}

/* footer */
.footer{position:absolute;left:0;top:3069px;width:1200px;height:278px;background:var(--footer);color:#e8e8e8}
.foot-links{position:absolute;top:126px;left:0;width:1200px;display:flex;justify-content:center;gap:28px;font-family:'Playfair Display',serif;font-size:13px}
.socials{position:absolute;top:164px;left:0;width:1200px;display:flex;justify-content:center;gap:29px}
.socials span{width:13px;height:13px;background:#f3f3f3;border-radius:3px}
.foot-line{position:absolute;left:0;top:234px;width:1200px;height:1px;background:#3b3938}
.copy{position:absolute;top:250px;left:0;width:1200px;text-align:center;font-size:11px}
</style>
</head>
<body>

<section class="hero">
  <div class="hero-photo" role="img" aria-label="Smiling patient in a dental chair giving a thumbs up with a dentist behind"></div>
  <div class="hero-shade"></div>
  <nav class="nav">
    <span class="logo">Maplecrest Dentistry</span>
    <div class="nav-links"><span>Home</span><span>Our Services</span><span>Contact Us</span></div>
  </nav>
  <h1>Premium <span class="accent">Dental Care</span> for<br>a Confident Smile</h1>
  <p>Expert cosmetic and restorative dentistry in a luxurious setting.</p>
  <a class="btn btn-teal abs" style="left:140px;top:320px;width:152px;height:38px">Book an Appointment</a>
  <a class="btn btn-white abs" style="left:305px;top:320px;width:107px;height:38px">View Services</a>
</section>

<form class="booking">
  <div class="field" style="left:22px"><div class="lbl">Name</div><div class="val">
    <svg width="13" height="13" viewBox="0 0 24 24" fill="none" stroke="#333" stroke-width="2"><circle cx="12" cy="8" r="4"/><path d="M4 21c1-5 15-5 16 0"/></svg>John Dee</div></div>
  <div class="divider" style="left:257px"></div>
  <div class="field" style="left:282px"><div class="lbl">Phone</div><div class="val">
    <svg width="13" height="13" viewBox="0 0 24 24" fill="none" stroke="#333" stroke-width="2"><path d="M5 3h4l2 5-3 2a11 11 0 0 0 6 6l2-3 5 2v4a2 2 0 0 1-2 2A17 17 0 0 1 3 5a2 2 0 0 1 2-2z"/></svg>Your Phone</div></div>
  <div class="divider" style="left:518px"></div>
  <div class="field" style="left:542px"><div class="lbl">Preferred Date</div><div class="val">
    <svg width="13" height="13" viewBox="0 0 24 24" fill="none" stroke="#333" stroke-width="2"><rect x="3" y="5" width="18" height="16" rx="2"/><path d="M3 10h18M8 3v4M16 3v4"/></svg>dd/mm/yyy</div></div>
  <a class="btn btn-teal abs" style="left:777px;top:22px;width:120px;height:38px">Book Now</a>
</form>

<h2 class="section-title" style="top:560px">Our Dental <u>Services</u></h2>
<p class="section-sub" style="top:604px;color:var(--muted)">Comprehensive, high-quality care from cosmetic enhancements to<br>emergency treatments—tailored to your smile.</p>

<div class="svc" style="left:140px;top:677px">
  <div class="ico"><svg width="26" height="26" viewBox="0 0 24 24" fill="none" stroke="#fff" stroke-width="1.6"><circle cx="12" cy="12" r="9"/><path d="M8 14c2 3 6 3 8 0"/><circle cx="9" cy="10" r=".6"/><circle cx="15" cy="10" r=".6"/></svg></div>
  <h3>Cosmetic Dentistry</h3><p>Enhance your smile with treatments that improve tooth shape, color, and appearance.</p></div>
<div class="svc" style="left:455px;top:677px">
  <div class="ico"><svg width="26" height="26" viewBox="0 0 24 24" fill="none" stroke="#fff" stroke-width="1.6"><path d="M7 4c2-1 3 0 5 0s3-1 5 0c1 2 0 5-1 6H8C7 9 6 6 7 4z"/><path d="M9 12h6M10 15h4M11 18h2M12 10v11"/></svg></div>
  <h3>Dental Implants</h3><p>Permanent, natural-looking tooth replacements that restore function and confidence.</p></div>
<div class="svc" style="left:768px;top:677px">
  <div class="ico"><svg width="26" height="26" viewBox="0 0 24 24" fill="none" stroke="#fff" stroke-width="1.6"><path d="M5 5l14 14M19 5L5 19"/><circle cx="5" cy="5" r="2"/><circle cx="19" cy="5" r="2"/></svg></div>
  <h3>Emergency Services</h3><p>Quick, professional treatment for dental emergencies, providing relief when you need it most.</p></div>
<div class="svc" style="left:140px;top:887px">
  <div class="ico"><svg width="26" height="26" viewBox="0 0 24 24" fill="none" stroke="#fff" stroke-width="1.6"><path d="M4 9c5 2 11 2 16 0-1 6-4 9-8 9s-7-3-8-9z"/><path d="M6 12h12M9 10v4M12 10v5M15 10v4"/></svg></div>
  <h3>Dentures</h3><p>Comfortable, custom-fitted full and partial dentures that restore your bite and your natural smile.</p></div>
<div class="svc" style="left:455px;top:887px">
  <div class="ico"><svg width="26" height="26" viewBox="0 0 24 24" fill="none" stroke="#fff" stroke-width="1.6"><path d="M7 3c2 0 3 1 5 1s3-1 5-1c3 0 4 4 2 9-1 3-1 9-3 9s-2-6-4-6-2 6-4 6-2-6-3-9C3 7 4 3 7 3z"/><path d="M16 6l1 1"/></svg></div>
  <h3>Dental Hygiene</h3><p>Preventive cleanings and exams to keep your teeth and gums healthy, fresh, and cavity-free.</p></div>
<div class="svc" style="left:768px;top:887px">
  <div class="ico"><svg width="26" height="26" viewBox="0 0 24 24" fill="none" stroke="#fff" stroke-width="1.6"><path d="M7 3c2 0 3 1 5 1s3-1 5-1c3 0 4 4 2 9-1 3-1 9-3 9s-2-6-4-6-2 6-4 6-2-6-3-9C3 7 4 3 7 3z"/></svg></div>
  <h3>Tooth Restoration</h3><p>Repair and restore damaged teeth with natural-looking fillings, crowns, and bridges for a healthier smile.</p></div>

<section class="why"></section>
<h2 class="section-title" style="top:1202px;color:var(--white)">Why <u>Choose</u> Us?</h2>
<p class="section-sub" style="top:1245px;color:#eef1f3">Experience expert care in a modern, comfort-first clinic—where<br>advanced technology meets personalized treatment.</p>

<div class="why-item" style="top:1332px"><div class="ico"><svg width="38" height="38" viewBox="0 0 24 24" fill="none" stroke="#5cc0b5" stroke-width="1.5"><rect x="3" y="4" width="18" height="15" rx="1"/><rect x="6" y="7" width="12" height="9"/><path d="M10 9c1 0 1 .5 2 .5s1-.5 2-.5c1 1 0 3-1 5h-2c-1-2-2-4-1-5z"/></svg></div>
  <h3>Board-Certified Dentists</h3><p>Expertise you can trust, backed by advanced training and credentials.</p></div>
<div class="why-item" style="top:1445px"><div class="ico"><svg width="38" height="38" viewBox="0 0 24 24" fill="none" stroke="#5cc0b5" stroke-width="1.5"><path d="M8 9c2 0 3 1 4 1s2-1 4-1c3 0 3 4 2 7-1 2-1 6-2 6s-2-4-4-4-2 4-3 4-1-4-2-6c-1-3-1-7 1-7z"/><path d="M9 2l5 4M12 2l2 2"/></svg></div>
  <h3>Pain-Free Treatments</h3><p>Gentle techniques and modern technology for a stress-free experience.</p></div>
<div class="why-item" style="top:1558px"><div class="ico"><svg width="38" height="38" viewBox="0 0 24 24" fill="none" stroke="#5cc0b5" stroke-width="1.5"><path d="M5 6c2-2 5-2 6 0"/><path d="M8 8l3 7h7l2 3M11 15l-2 6M6 21h8"/><circle cx="17" cy="8" r="2"/></svg></div>
  <h3>Luxury, Comfort-First Clinic</h3><p>Designed to help you relax—because your comfort matters.</p></div>
<div class="why-item" style="top:1671px"><div class="ico"><svg width="38" height="38" viewBox="0 0 24 24" fill="#5cc0b5"><path d="M4 9h14a2 2 0 0 1 2 2v8a2 2 0 0 1-2 2H4z"/><path d="M6 8l9-4 2 4z"/><circle cx="17" cy="15" r="1.5" fill="#fff"/></svg></div>
  <h3>Flexible Payment Plans</h3><p>Quality care made accessible with tailored financing options.</p></div>

<div class="why-photo"><div class="fill" role="img" aria-label="Smiling dentist in a white coat with arms crossed in a clinic"></div></div>

<h2 class="section-title" style="top:1910px">Visit Our <u>Clinic</u></h2>
<p class="section-sub" style="top:1953px;color:var(--muted)">Located in the heart of Maplecrest, our clinic offers flexible hours and easy<br>access to premium dental care.</p>

<div class="map" role="img" aria-label="Street map showing the clinic location"></div>
<aside class="info">
  <h4><svg width="18" height="18" viewBox="0 0 24 24" fill="none" stroke="#5cc0b5" stroke-width="1.8"><path d="M12 21s-7-6-7-12a7 7 0 0 1 14 0c0 6-7 12-7 12z"/><circle cx="12" cy="9" r="2.5"/></svg>Visit Us</h4>
  <p style="padding-left:8px">48 Harbor View Road, Maplecrest</p>
  <h4 style="margin-top:22px"><svg width="18" height="18" viewBox="0 0 24 24" fill="none" stroke="#5cc0b5" stroke-width="1.8"><circle cx="12" cy="12" r="9"/><path d="M12 7v5l3 2"/></svg>Operating Hours</h4>
  <p>Mon–Fri: 8:00 AM – 6:00 PM<br>Sat: 9:00 AM – 2:00 PM<br>Closed Sundays</p>
  <h4 style="margin-top:20px"><svg width="18" height="18" viewBox="0 0 24 24" fill="none" stroke="#5cc0b5" stroke-width="1.8"><path d="M5 3h4l2 5-3 2a11 11 0 0 0 6 6l2-3 5 2v4a2 2 0 0 1-2 2A17 17 0 0 1 3 5a2 2 0 0 1 2-2z"/></svg>Call Us</h4>
  <p>(555) 214-3380</p>
  <a class="btn btn-white" style="margin-top:14px;width:94px;height:32px;font-size:12px;color:var(--ink)">Call Now</a>
</aside>

<section class="reviews"></section>
<h2 class="section-title" style="top:2613px;color:var(--white)">What Our Patients <u>Say</u></h2>
<p class="section-sub" style="top:2657px;color:#eef1f3">Real stories from patients who've experienced compassionate care,<br>outstanding results, and a confident new smile.</p>

<div class="arrow" style="left:91px;border:1.5px solid #fff"><svg width="14" height="14" viewBox="0 0 24 24" fill="none" stroke="#fff" stroke-width="2.5"><path d="M15 5l-7 7 7 7"/></svg></div>
<div class="arrow" style="left:1080px;background:#fff"><svg width="14" height="14" viewBox="0 0 24 24" fill="none" stroke="#1f2a36" stroke-width="2.5"><path d="M9 5l7 7-7 7"/></svg></div>

<article class="review" style="left:140px">
  <div class="stars">
    <svg width="21" height="20" viewBox="0 0 24 24" fill="#d6a93a"><path d="M12 2l3 7 7 .5-5.5 4.5 2 7.5L12 17l-6.5 4.5 2-7.5L2 9.5 9 9z"/></svg><svg width="21" height="20" viewBox="0 0 24 24" fill="#d6a93a"><path d="M12 2l3 7 7 .5-5.5 4.5 2 7.5L12 17l-6.5 4.5 2-7.5L2 9.5 9 9z"/></svg><svg width="21" height="20" viewBox="0 0 24 24" fill="#d6a93a"><path d="M12 2l3 7 7 .5-5.5 4.5 2 7.5L12 17l-6.5 4.5 2-7.5L2 9.5 9 9z"/></svg><svg width="21" height="20" viewBox="0 0 24 24" fill="#d6a93a"><path d="M12 2l3 7 7 .5-5.5 4.5 2 7.5L12 17l-6.5 4.5 2-7.5L2 9.5 9 9z"/></svg><svg width="21" height="20" viewBox="0 0 24 24" fill="#d6a93a"><path d="M12 2l3 7 7 .5-5.5 4.5 2 7.5L12 17l-6.5 4.5 2-7.5L2 9.5 9 9z"/></svg>
  </div>
  <span class="date">10th Feb, 2023</span>
  <p class="quote">"The team made me feel comfortable from the moment I walked in. My smile has never looked better!"</p>
  <div class="who"><div class="avatar" role="img" aria-label="Portrait of the reviewer" style="background:linear-gradient(135deg,#c9d2d6,#8f7a6a)"></div><div><div class="name">Daniel R.</div><div class="role">Customer</div></div></div>
</article>
<article class="review" style="left:610px">
  <div class="stars">
    <svg width="21" height="20" viewBox="0 0 24 24" fill="#d6a93a"><path d="M12 2l3 7 7 .5-5.5 4.5 2 7.5L12 17l-6.5 4.5 2-7.5L2 9.5 9 9z"/></svg><svg width="21" height="20" viewBox="0 0 24 24" fill="#d6a93a"><path d="M12 2l3 7 7 .5-5.5 4.5 2 7.5L12 17l-6.5 4.5 2-7.5L2 9.5 9 9z"/></svg><svg width="21" height="20" viewBox="0 0 24 24" fill="#d6a93a"><path d="M12 2l3 7 7 .5-5.5 4.5 2 7.5L12 17l-6.5 4.5 2-7.5L2 9.5 9 9z"/></svg><svg width="21" height="20" viewBox="0 0 24 24" fill="#d6a93a"><path d="M12 2l3 7 7 .5-5.5 4.5 2 7.5L12 17l-6.5 4.5 2-7.5L2 9.5 9 9z"/></svg><svg width="21" height="20" viewBox="0 0 24 24" fill="#d6a93a"><path d="M12 2l3 7 7 .5-5.5 4.5 2 7.5L12 17l-6.5 4.5 2-7.5L2 9.5 9 9z"/></svg>
  </div>
  <span class="date">06th Feb, 2023</span>
  <p class="quote">"Beautiful clinic, friendly staff, and pain-free treatment. Truly a premium dental experience."</p>
  <div class="who"><div class="avatar" role="img" aria-label="Portrait of the reviewer" style="background:linear-gradient(135deg,#e8c94a,#c99b7a)"></div><div><div class="name">Olivia K.</div><div class="role">Customer</div></div></div>
</article>

<a class="btn btn-teal abs" style="left:547px;top:2965px;width:105px;height:39px">View All</a>

<footer class="footer">
  <div class="logo" style="position:absolute;top:60px;left:0;width:1200px;text-align:center;font-size:24px">Maplecrest Dentistry</div>
  <div class="foot-links"><span>Home</span><span>Our Services</span><span>Contact Us</span></div>
  <div class="socials"><span aria-label="Social profile"></span><span aria-label="Social profile"></span><span aria-label="Social profile"></span></div>
  <div class="foot-line"></div>
  <div class="copy">© 2025 Maplecrest dentistry. All Rights Reserved.</div>
</footer>

</body>
</html>
```